Flyer für Abschleppunternehmen
Zielgruppe
Abschleppunternehmen mit diversen Leistungen. Abschleppen, bergen, pannnenhilfe, transport von LKW und PKW,
Falschparker, Kranservice, etc.
Aufgabenstellung
übersichtlich nicht zu viel Text, Bilder mit einarbeiten, evlt Freistehende Fahrzeuge. Vorstellung des Betriebs

```html
<!DOCTYPE html>
<html lang="de">
<head>
<meta charset="utf-8">
<title>Brandauer Abschleppdienst – Flyer</title>
<link href="https://fonts.googleapis.com/css2?family=Archivo+Black&family=Roboto:ital,wght@0,500;1,700&family=Roboto+Condensed:wght@400;500&display=swap" rel="stylesheet">
<style>
  :root{
    --yellow:#ffcc00;
    --red:#d9161c;
    --ink:#111111;
    --text:#3a3a3a;
    --paper:#ffffff;
    --mist:#eef0f2;
    --sky:#9fb9d8;
    --sky-pale:#dfe7ee;
    --truck:#f2cf1c;
    --asphalt:#4d4f52;
    --leaf:#8a6a3a;
    --grass:#7c9a55;
  }
  *{margin:0;padding:0;box-sizing:border-box}
  html,body{width:1200px;height:853px;overflow:hidden;background:var(--paper)}
  body{position:relative;font-family:"Roboto",sans-serif}

  .page{position:absolute;top:42px;width:543px;height:768px;overflow:hidden;background:var(--mist);box-shadow:0 0 8px rgba(0,0,0,.25)}
  .page--front{left:38px}
  .page--back{left:619px;width:531px}

  .bg-photo{position:absolute;inset:0}
  .page--front .bg-photo{
    background:
      linear-gradient(90deg,rgba(245,246,247,.92) 0%,rgba(245,246,247,.6) 60%,rgba(245,246,247,.85) 100%),
      linear-gradient(180deg,#e4e8ec 0%,#e4e8ec 30%,#f0dd86 42%,#f3e4a0 58%,#e6e3d8 70%,#d9dbdd 100%);
  }
  .page--back .bg-photo{
    background:
      linear-gradient(180deg,rgba(236,238,240,.55) 0%,rgba(236,238,240,.35) 100%),
      linear-gradient(180deg,#cfd5db 0%,#d6d9d5 28%,#f0d95a 40%,#f2de70 62%,#e6dca2 74%,#c9cccd 88%,#b9bcbe 100%);
  }

  .circle{position:absolute;border-radius:50%}
  .ring{background:var(--yellow)}
  .photo--crane{background:linear-gradient(180deg,var(--sky-pale) 0%,#c8d6e4 22%,var(--truck) 38%,#e6be12 62%,#2b2b2b 74%,var(--asphalt) 84%,#6a6d70 100%)}
  .photo--trucks{background:linear-gradient(180deg,#8fb0d6 0%,#c8d4df 30%,var(--truck) 42%,#f0c800 66%,#333 76%,#a39a8a 88%,#b8b2a4 100%)}
  .photo--sweeper{background:linear-gradient(180deg,#dfe3e6 0%,#c9ccce 18%,var(--truck) 32%,#e9c70e 58%,#3a3c3e 72%,#6d5c42 86%,var(--leaf) 100%)}
  .photo--crane-arm{background:linear-gradient(160deg,#4f7fc4 0%,#8fb2de 35%,var(--truck) 50%,#d8b30a 70%,#5c5e60 88%,#8a8c8e 100%)}

  .frame{position:absolute;background:var(--yellow)}

  .brand{position:absolute;display:flex;align-items:center;gap:8px}
  .brand__dot{width:16px;height:16px;border-radius:50%;background:var(--red)}
  .brand__name{font-family:"Roboto",sans-serif;font-weight:500;font-size:24px;color:var(--ink);letter-spacing:.5px}

  .headline{position:absolute;font-family:"Archivo Black",sans-serif;font-size:48px;line-height:1;color:var(--ink);
    text-shadow:1.5px 1.5px 0 var(--yellow),-1px -1px 0 var(--yellow),1px -1px 0 var(--yellow),-1px 1px 0 var(--yellow)}
  .since{position:absolute;left:58px;top:330px;font-family:"Roboto",sans-serif;font-weight:500;font-size:22px;color:var(--ink)}

  .services-title{position:absolute;left:55px;top:374px;width:247px;height:27px;border-radius:14px;background:var(--yellow);
    font-style:italic;font-weight:700;font-size:14px;letter-spacing:.6px;color:#2a2a2a;line-height:27px;text-align:center}
  .services{position:absolute;left:73px;top:413px;list-style:none}
  .services li{display:flex;align-items:center;gap:10px;height:27.3px;font-family:"Roboto Condensed",sans-serif;font-size:15px;color:var(--text)}
  .services svg{width:18px;height:18px;flex:none}

  .badge{position:absolute;width:80px;height:80px;border-radius:50%;background:var(--red);display:flex;align-items:center;justify-content:center}
  .badge__text{color:#fff;text-align:center;font-family:"Roboto",sans-serif;font-weight:700;font-style:italic;transform:rotate(-18deg);line-height:1}
  .badge__text b{display:block;font-size:17px}
  .badge__text span{display:block;font-size:8px;letter-spacing:.5px}
  .badge__arc{position:absolute;inset:12px;border:2.5px solid #fff;border-radius:50%;border-left-color:transparent}

  .promise{position:absolute;left:23px;top:272px;width:296px;height:296px;border-radius:50%;background:var(--paper);
    display:flex;align-items:center;justify-content:center;padding:0 22px;text-align:center;
    font-family:"Roboto Condensed",sans-serif;font-weight:500;font-size:21.5px;line-height:24.5px;color:var(--ink)}
  .promise-ring{left:13px;top:262px;width:316px;height:316px}

  .transport-photo{position:absolute;left:0;top:563px;width:531px;height:193px;
    background:linear-gradient(180deg,#b9c7d6 0%,#d3dae1 25%,#9aa0a4 42%,#8d9193 55%,#e5c21a 64%,#777b7d 74%,#a9adaf 84%,var(--grass) 100%)}
</style>
</head>
<body>

<section class="page page--front">
  <div class="bg-photo" role="img" aria-label="Blasses Hintergrundfoto eines gelben Abschleppfahrzeugs"></div>

  <div class="frame" style="left:0;top:0;width:225px;height:10px"></div>
  <div class="frame" style="left:0;top:0;width:10px;height:768px"></div>
  <div class="frame" style="left:248px;top:758px;width:295px;height:10px"></div>

  <div class="circle ring" style="left:204px;top:-38px;width:350px;height:350px"></div>
  <div class="circle photo--crane" role="img" aria-label="Foto: gelber Mobilkran vor dem Firmengelände" style="left:217px;top:-25px;width:324px;height:324px"></div>

  <div class="brand" style="left:34px;top:60px">
    <span class="brand__dot"></span><span class="brand__name">Brandauer</span>
  </div>

  <div class="headline" style="left:59px;top:166px">WIR</div>
  <div class="headline" style="left:81px;top:220px">SIND</div>
  <div class="headline" style="left:134px;top:272px">DA!</div>

  <div class="since">SEIT ÜBER 50 JAHREN</div>

  <div class="services-title">Unsere Leistungen und Services</div>
  <ul class="services">
    <li><svg viewBox="0 0 18 18"><circle cx="9" cy="9" r="9" fill="#ffcc00"/><path d="M5 9.3l2.7 2.6L13 6.5" fill="none" stroke="#fff" stroke-width="2.2" stroke-linecap="round" stroke-linejoin="round"/></svg>Abschleppen/Bergen</li>
    <li><svg viewBox="0 0 18 18"><circle cx="9" cy="9" r="9" fill="#ffcc00"/><path d="M5 9.3l2.7 2.6L13 6.5" fill="none" stroke="#fff" stroke-width="2.2" stroke-linecap="round" stroke-linejoin="round"/></svg>Pannenservice</li>
    <li><svg viewBox="0 0 18 18"><circle cx="9" cy="9" r="9" fill="#ffcc00"/><path d="M5 9.3l2.7 2.6L13 6.5" fill="none" stroke="#fff" stroke-width="2.2" stroke-linecap="round" stroke-linejoin="round"/></svg>Fahrzeugtransport</li>
    <li><svg viewBox="0 0 18 18"><circle cx="9" cy="9" r="9" fill="#ffcc00"/><path d="M5 9.3l2.7 2.6L13 6.5" fill="none" stroke="#fff" stroke-width="2.2" stroke-linecap="round" stroke-linejoin="round"/></svg>Kranservice</li>
    <li><svg viewBox="0 0 18 18"><circle cx="9" cy="9" r="9" fill="#ffcc00"/><path d="M5 9.3l2.7 2.6L13 6.5" fill="none" stroke="#fff" stroke-width="2.2" stroke-linecap="round" stroke-linejoin="round"/></svg>Fahrzeugöffnung</li>
    <li><svg viewBox="0 0 18 18"><circle cx="9" cy="9" r="9" fill="#ffcc00"/><path d="M5 9.3l2.7 2.6L13 6.5" fill="none" stroke="#fff" stroke-width="2.2" stroke-linecap="round" stroke-linejoin="round"/></svg>Tiefgaragenservice</li>
    <li><svg viewBox="0 0 18 18"><circle cx="9" cy="9" r="9" fill="#ffcc00"/><path d="M5 9.3l2.7 2.6L13 6.5" fill="none" stroke="#fff" stroke-width="2.2" stroke-linecap="round" stroke-linejoin="round"/></svg>Falschparker</li>
  </ul>

  <div class="badge" style="left:257px;top:539px"><span class="badge__arc"></span><span class="badge__text"><b>24/7</b><span>SERVICE</span></span></div>

  <div class="circle ring" style="left:355px;top:302px;width:194px;height:194px"></div>
  <div class="circle photo--trucks" role="img" aria-label="Foto: zwei gelbe Abschlepp-Lkw nebeneinander" style="left:357px;top:312px;width:184px;height:184px"></div>

  <div class="circle ring" style="left:355px;top:545px;width:194px;height:194px"></div>
  <div class="circle photo--sweeper" role="img" aria-label="Foto: gelbe Kehrmaschine für Straßenreinigung" style="left:357px;top:553px;width:184px;height:184px"></div>

  <div class="circle ring" style="left:3px;top:616px;width:234px;height:234px"></div>
  <div class="circle photo--crane-arm" role="img" aria-label="Foto: Mobilkran mit ausgefahrenem Ausleger" style="left:-2px;top:640px;width:204px;height:204px"></div>
</section>

<section class="page page--back">
  <div class="bg-photo" role="img" aria-label="Blasses Hintergrundfoto eines großen gelben Abschlepp-Lkw"></div>

  <div class="frame" style="left:521px;top:0;width:10px;height:768px"></div>

  <div class="circle ring" style="left:-31px;top:-29px;width:290px;height:290px"></div>
  <div class="circle photo--sweeper" role="img" aria-label="Foto: gelbe Kehrmaschine auf nassem Asphalt" style="left:-19px;top:-17px;width:266px;height:266px"></div>

  <div class="circle ring" style="left:305px;top:-151px;width:234px;height:234px"></div>

  <div class="brand" style="left:352px;top:60px">
    <span class="brand__dot"></span><span class="brand__name">Brandauer</span>
  </div>

  <div class="circle ring promise-ring"></div>
  <p class="promise">Egal wann und wo sie uns brauchen, wir sind an allen Tagen das ganze Jahr über im 24 Stunden Service ihr Ansprechpartner nach Unfall oder Panne mit PKW,LKW oder Motorrad.</p>

  <div class="badge" style="left:437px;top:466px"><span class="badge__arc"></span><span class="badge__text"><b>24/7</b><span>SERVICE</span></span></div>

  <div class="frame" style="left:0;top:559px;width:531px;height:4px"></div>
  <div class="transport-photo" role="img" aria-label="Foto: Autotransporter mit zwei grauen Transportern"></div>
  <div class="frame" style="left:0;top:756px;width:531px;height:12px"></div>
</section>

</body>
</html>
```